Fruits and Vegetables distribution company needs a new eye catching website

We need to get our website up to date. Our clients will look at our website to learn about our products and services. Our design needs to be simple yet impactful to make our brand memorable to our visitors. We need to have somewhere to tell our clients about our history, products and services, our team. We can throw in a few fun facts and figures and maybe some testimonials to impress. We have 4 theme colors that we want to incorporate into the design, you can get in touch for the HEX/RGB codes. Please remember that smooth operation of any animations and interactions is very important.

```html
<!DOCTYPE html>
<html lang="en">
<head>
<meta charset="utf-8">
<title>Sahara Harvest – Fresh Fruits &amp; Vegetables</title>
<link rel="stylesheet" href="https://fonts.googleapis.com/css2?family=Cinzel:wght@400;700&family=Lato:wght@400;700&display=swap">
<style>
:root{
  --green:#8cc63e;
  --red:#c4262e;
  --red-dark:#a51e25;
  --orange:#f7a400;
  --orange-dark:#e88f00;
  --ink:#333333;
  --muted:#888888;
  --line:#dddddd;
  --paper:#ffffff;
  --strip:#eeeeee;
  --footer:#2e2e2e;
  --footer-deep:#222222;
}
*{box-sizing:border-box;margin:0;padding:0}
html,body{width:1200px;height:4864px;overflow:hidden}
body{font-family:"Lato",Arial,sans-serif;color:var(--ink);background:var(--paper);position:relative}
section,header,footer{position:absolute;left:0;width:1200px}
.heading{font-family:"Cinzel",Georgia,serif;font-weight:700;letter-spacing:2px}

/* hero */
.hero{top:0;height:800px;overflow:hidden}
.hero-visual{position:absolute;inset:0;background:
  radial-gradient(circle at 15% 30%,#6f9a2c 0,transparent 35%),
  radial-gradient(circle at 80% 25%,#e0421c 0,transparent 35%),
  radial-gradient(circle at 60% 75%,#d8a21d 0,transparent 35%),
  radial-gradient(circle at 25% 80%,#b8361f 0,transparent 40%),
  linear-gradient(135deg,#7a3a20,#8a5a25 50%,#5e7a25)}
.hero-visual::after{content:"";position:absolute;inset:0;background:rgba(0,0,0,.28)}
.nav{position:absolute;top:44px;left:0;width:1200px;display:flex;justify-content:center;align-items:flex-start;gap:0}
.nav ul{list-style:none;display:flex;gap:30px;color:#fff;font-size:15px;padding-top:14px}
.nav ul.left{margin-right:44px}
.nav ul.right{margin-left:44px}
.brand{width:170px;height:110px;background:#fff;display:flex;flex-direction:column;align-items:center;justify-content:center;gap:8px;margin-top:-44px}
.brand-dot{width:34px;height:34px;border-radius:50%;background:var(--orange)}
.brand-name{font-family:"Lato",Arial,sans-serif;font-weight:700;font-size:15px;letter-spacing:1px;color:var(--red)}
.play{position:absolute;left:540px;top:260px}
.hero-tag{position:absolute;top:392px;width:100%;text-align:center;color:#fff;font-size:15px;font-weight:700;letter-spacing:2px}

/* history */
.history{top:800px;height:180px;background:var(--green);text-align:center;color:#fff}
.history .welcome{margin-top:30px;font-size:14px}
.history h2{font-size:26px;margin-top:4px;color:#fff}
.history h2 span{color:var(--red)}
.history p{width:560px;margin:16px auto 0;font-size:13px;line-height:1.5}
.btn{display:inline-block;border:2px solid var(--red);color:var(--red);font-size:12px;font-weight:700;letter-spacing:1px;padding:9px 22px;background:transparent}
.history .btn{margin-top:14px;border-color:var(--red);color:var(--red)}

/* section title */
.section-title{display:flex;align-items:center;justify-content:center;gap:24px}
.section-title .rule{width:210px;height:1px;background:var(--orange)}
.section-title h2{position:relative;font-size:24px;padding:0 22px;z-index:1}
.section-title h2::before{content:"";position:absolute;left:50%;top:50%;width:44px;height:44px;background:var(--orange);transform:translate(-50%,-50%) rotate(45deg);z-index:-1;opacity:.9}
.section-title.light .rule{background:#fff}
.section-title.light h2{color:#fff}

/* products */
.products{top:980px;height:1080px}
.products .section-title{margin-top:52px}
.tabs{display:flex;justify-content:center;margin-top:44px}
.tab{width:140px;height:40px;display:flex;align-items:center;justify-content:center;font-size:12px;font-weight:700;letter-spacing:1px;border:2px solid var(--green)}
.tab.active{background:var(--green);color:#fff}
.tab.idle{color:var(--green);background:#fff}
.grid{position:absolute;top:216px;left:124px;display:grid;grid-template-columns:repeat(4,232px);column-gap:8px;row-gap:40px}
.card{width:232px;border:1px solid var(--line);padding:4px 4px 0;height:326px;position:relative}
.card .photo{width:222px;height:230px}
.card .name{text-align:center;font-family:"Cinzel",Georgia,serif;font-weight:700;font-size:15px;letter-spacing:2px;margin-top:20px}
.card .more{position:absolute;left:0;right:0;bottom:0;height:44px;display:flex;align-items:center;justify-content:center}
.card .more::before{content:"";position:absolute;left:12px;right:12px;top:22px;height:1px;background:var(--line)}
.card svg{position:relative}
.products .view{position:absolute;top:956px;left:546px}

/* services */
.services{top:2060px;height:580px;background:
  radial-gradient(circle at 30% 70%,rgba(255,255,255,.08),transparent 50%),
  linear-gradient(180deg,var(--red),var(--red-dark));text-align:center;color:#fff}
.services .section-title{margin-top:36px}
.services p{width:560px;margin:40px auto 0;font-size:13px;line-height:1.5}
.world{position:absolute;left:240px;top:220px;width:720px;height:290px;border-radius:60px;background:rgba(255,255,255,.82)}

/* team */
.team{top:2640px;height:600px}
.team .section-title{margin-top:64px}
.member{position:absolute;top:176px;width:300px;text-align:center}
.portrait{width:248px;height:248px;border-radius:50%;border:3px solid #f5b5b5;margin:0 auto;padding:10px;background:#fff}
.portrait div{width:100%;height:100%;border-radius:50%}
.socials{position:absolute;top:0;right:6px;display:flex;flex-direction:column;gap:10px}
.socials span{width:28px;height:28px;border-radius:50%;background:var(--orange);display:block}
.socials span:nth-child(1){transform:translate(-8px,14px)}
.socials span:nth-child(2){transform:translate(6px,14px)}
.socials span:nth-child(3){transform:translate(10px,14px)}
.socials span:nth-child(4){transform:translate(6px,14px)}
.socials span:nth-child(5){transform:translate(-8px,14px)}
.member h3{font-family:"Cinzel",Georgia,serif;font-size:17px;letter-spacing:2px;margin-top:22px}
.member .role{color:var(--green);font-size:12px;margin-top:6px}
.team .view{position:absolute;top:552px;left:546px}

/* testimonials */
.testimonials{top:3240px;height:520px;background:linear-gradient(180deg,var(--orange),var(--orange-dark));text-align:center;color:#fff}
.testimonials .section-title{margin-top:84px}
.testimonials .section-title h2::before{background:var(--green)}
.quote-mark{font-family:Georgia,serif;font-size:80px;line-height:1;margin-top:24px;color:var(--ink)}
.testimonials p{width:600px;margin:0 auto;font-size:13px;line-height:1.5}
.testimonials h4{font-family:"Cinzel",Georgia,serif;font-size:17px;letter-spacing:2px;margin-top:16px;color:var(--ink)}
.testimonials .who{font-size:12px;margin-top:4px}
.pager{display:flex;justify-content:center;align-items:center;gap:14px;margin-top:22px}
.pager i{display:block;width:8px;height:8px;border-radius:50%;background:#fff}
.pager i.on{background:var(--red)}
.testimonials .btn{margin-top:24px}

/* contact */
.contact{top:3760px;height:488px}
.contact .section-title{margin-top:60px}
.form{position:absolute;left:300px;top:136px;width:600px;display:grid;grid-template-columns:1fr 1fr;gap:12px 16px}
.field{height:40px;border:1px solid var(--line);font-size:12px;color:#aaa;padding:12px 12px}
.field.wide{grid-column:1/3}
.field.msg{height:100px}
.contact .submit{position:absolute;left:552px;top:436px;font-size:11px;padding:8px 22px}

/* partners */
.partners{top:4248px;height:244px;background:var(--strip)}
.partner-row{position:absolute;top:66px;left:140px;display:flex;gap:52px;align-items:center}
.badge{width:196px;height:112px;background:#fff;border:1px solid var(--line);display:flex;align-items:center;justify-content:center}
.badge div{width:130px;height:54px;border-radius:6px}
.arrow{position:absolute;top:108px}

/* footer */
.site-footer{top:4492px;height:372px;background:var(--footer);color:#ddd}
.f-about{position:absolute;left:112px;top:40px;width:200px}
.f-brand{display:flex;align-items:center;gap:10px}
.f-brand .brand-dot{width:26px;height:26px}
.f-brand span{font-weight:700;font-size:14px;letter-spacing:1px;color:#fff}
.f-about p{font-size:12px;line-height:1.5;margin-top:14px;color:#ccc}
.f-about .readmore{color:var(--red);font-size:11px;font-weight:700;margin-top:8px;display:block}
.f-social{display:flex;gap:10px;margin-top:14px}
.f-social i{width:14px;height:14px;border-radius:50%;background:var(--orange);display:block}
.f-col{position:absolute;top:50px}
.f-col h5{font-family:"Cinzel",Georgia,serif;font-size:22px;color:#fff;letter-spacing:1px;margin-bottom:24px}
.f-col ul{list-style:none;font-size:12px;line-height:1.9;color:#ccc}
.f-contact li{display:flex;align-items:center;gap:8px}
.bottom{position:absolute;left:0;bottom:0;width:1200px;height:64px;background:var(--footer-deep);display:flex;justify-content:space-between;align-items:center;padding:0 112px;font-size:12px;color:#aaa}
</style>
</head>
<body>

<header class="hero">
  <div class="hero-visual" role="img" aria-label="Heap of fresh fruits and vegetables"></div>
  <nav class="nav">
    <ul class="left"><li>Home</li><li>About us</li><li>Products</li></ul>
    <div class="brand"><span class="brand-dot"></span><span class="brand-name">SAHARA HARVEST</span></div>
    <ul class="right"><li>Services</li><li>Our Team</li><li>Contact Us</li></ul>
  </nav>
  <svg class="play" width="120" height="120" viewBox="0 0 120 120" aria-label="Play video">
    <circle cx="60" cy="60" r="56" fill="none" stroke="#fff" stroke-width="4"/>
    <path d="M48 38 L84 60 L48 82 Z" fill="none" stroke="#fff" stroke-width="4" stroke-linejoin="round"/>
  </svg>
  <div class="hero-tag">WE ARE LARGEST DISTRIBUTE FRESH FRUITS &amp; VEGETABLE</div>
</header>

<section class="history">
  <div class="welcome">Welcome to Sahara Harvest</div>
  <h2 class="heading">OUR <span>HISTORY</span></h2>
  <p>Since our first market stall, we have carried fresh produce from trusted farms to kitchens across the region, keeping every crate crisp, ripe and on time.</p>
  <span class="btn">READ MORE</span>
</section>

<section class="products">
  <div class="section-title"><span class="rule"></span><h2 class="heading">OUR PRODUCTS</h2><span class="rule"></span></div>
  <div class="tabs"><span class="tab active">FRUITS</span><span class="tab idle">VEGETABLES</span></div>
  <div class="grid">
    <article class="card"><div class="photo" role="img" aria-label="Apples" style="background:linear-gradient(135deg,#c8242a,#e8703a)"></div><div class="name">APPLES</div><div class="more"><svg width="24" height="24"><circle cx="12" cy="12" r="11" fill="#fff" stroke="#c4262e" stroke-width="2"/><path d="M12 7v10M7 12h10" stroke="#c4262e" stroke-width="2"/></svg></div></article>
    <article class="card"><div class="photo" role="img" aria-label="Bananas" style="background:linear-gradient(135deg,#e8d44a,#a3a33a)"></div><div class="name">BANANAS</div><div class="more"><svg width="24" height="24"><circle cx="12" cy="12" r="11" fill="#fff" stroke="#8cc63e" stroke-width="2"/><path d="M12 7v10M7 12h10" stroke="#8cc63e" stroke-width="2"/></svg></div></article>
    <article class="card"><div class="photo" role="img" aria-label="Strawberries" style="background:linear-gradient(135deg,#d81f26,#a8141a)"></div><div class="name">STRAWBERRIES</div><div class="more"><svg width="24" height="24"><circle cx="12" cy="12" r="11" fill="#fff" stroke="#c4262e" stroke-width="2"/><path d="M12 7v10M7 12h10" stroke="#c4262e" stroke-width="2"/></svg></div></article>
    <article class="card"><div class="photo" role="img" aria-label="Pineapples" style="background:linear-gradient(135deg,#3f6a3a,#b07a32)"></div><div class="name">PINEAPPLES</div><div class="more"><svg width="24" height="24"><circle cx="12" cy="12" r="11" fill="#fff" stroke="#c4262e" stroke-width="2"/><path d="M12 7v10M7 12h10" stroke="#c4262e" stroke-width="2"/></svg></div></article>
    <article class="card"><div class="photo" role="img" aria-label="Melons" style="background:linear-gradient(135deg,#2f5a2a,#5e8a3a)"></div><div class="name">MELONS</div><div class="more"><svg width="24" height="24"><circle cx="12" cy="12" r="11" fill="#fff" stroke="#c4262e" stroke-width="2"/><path d="M12 7v10M7 12h10" stroke="#c4262e" stroke-width="2"/></svg></div></article>
    <article class="card"><div class="photo" role="img" aria-label="Kiwifruits" style="background:linear-gradient(135deg,#9cbf3a,#6e8a2a)"></div><div class="name">KIWIFRUITS</div><div class="more"><svg width="24" height="24"><circle cx="12" cy="12" r="11" fill="#fff" stroke="#c4262e" stroke-width="2"/><path d="M12 7v10M7 12h10" stroke="#c4262e" stroke-width="2"/></svg></div></article>
    <article class="card"><div class="photo" role="img" aria-label="Grapes" style="background:linear-gradient(135deg,#4a1f2e,#8a3a4a)"></div><div class="name">GRAPES</div><div class="more"><svg width="24" height="24"><circle cx="12" cy="12" r="11" fill="#fff" stroke="#c4262e" stroke-width="2"/><path d="M12 7v10M7 12h10" stroke="#c4262e" stroke-width="2"/></svg></div></article>
    <article class="card"><div class="photo" role="img" aria-label="Plums" style="background:linear-gradient(135deg,#b01a2a,#7a1020)"></div><div class="name">PLUMS</div><div class="more"><svg width="24" height="24"><circle cx="12" cy="12" r="11" fill="#fff" stroke="#c4262e" stroke-width="2"/><path d="M12 7v10M7 12h10" stroke="#c4262e" stroke-width="2"/></svg></div></article>
  </div>
  <span class="btn view">VIEW MORE</span>
</section>

<section class="services">
  <div class="section-title light"><span class="rule"></span><h2 class="heading">OUR SERVICES</h2><span class="rule"></span></div>
  <p>Cold-chain transport, bulk sourcing and daily deliveries link growers on every continent with retailers, hotels and restaurants that count on steady quality.</p>
  <div class="world" role="img" aria-label="World map with delivery locations marked"></div>
</section>

<section class="team">
  <div class="section-title"><span class="rule"></span><h2 class="heading">OUR TEAM</h2><span class="rule"></span></div>
  <div class="member" style="left:90px">
    <div class="portrait"><div role="img" aria-label="Portrait of Adam Fielding" style="background:linear-gradient(160deg,#d9d4cc,#8a8580)"></div></div>
    <div class="socials"><span></span><span></span><span></span><span></span><span></span></div>
    <h3>ADAM FIELDING</h3><div class="role">Sales Head</div>
  </div>
  <div class="member" style="left:450px">
    <div class="portrait"><div role="img" aria-label="Portrait of Nora Bell" style="background:linear-gradient(160deg,#e6ddd2,#a0784e)"></div></div>
    <div class="socials"><span></span><span></span><span></span><span></span><span></span></div>
    <h3>NORA BELL</h3><div class="role">Buyer</div>
  </div>
  <div class="member" style="left:802px">
    <div class="portrait"><div role="img" aria-label="Portrait of Owen Marsh" style="background:linear-gradient(160deg,#d4d6d8,#4a5260)"></div></div>
    <div class="socials"><span></span><span></span><span></span><span></span><span></span></div>
    <h3>OWEN MARSH</h3><div class="role">Logistics</div>
  </div>
  <span class="btn view">VIEW MORE</span>
</section>

<section class="testimonials">
  <div class="section-title light"><span class="rule"></span><h2 class="heading">TESTIMONIALS</h2><span class="rule"></span></div>
  <div class="quote-mark">&ldquo;</div>
  <p>Their fruit arrives fresh every single morning, and the team always finds a way to fill an urgent order. A partner we truly rely on.</p>
  <h4>LEON CARTER</h4>
  <div class="who">Client</div>
  <div class="pager">
    <svg width="16" height="12"><path d="M15 6H2M6 1 1 6l5 5" fill="none" stroke="#333" stroke-width="2"/></svg>
    <i class="on"></i><i></i><i></i>
    <svg width="16" height="12"><path d="M1 6h13M10 1l5 5-5 5" fill="none" stroke="#333" stroke-width="2"/></svg>
  </div>
  <span class="btn">VIEW MORE</span>
</section>

<section class="contact">
  <div class="section-title"><span class="rule"></span><h2 class="heading">CONTACT US</h2><span class="rule"></span></div>
  <div class="form">
    <div class="field">First Name</div><div class="field">Last Name</div>
    <div class="field">Phone</div><div class="field">Email</div>
    <div class="field wide">Subject</div>
    <div class="field wide msg">Message</div>
  </div>
  <span class="btn submit">SUBMIT</span>
</section>

<section class="partners">
  <svg class="arrow" style="left:60px" width="30" height="20"><path d="M28 10H3M11 2 3 10l8 8" fill="none" stroke="#333" stroke-width="2.5"/></svg>
  <div class="partner-row">
    <div class="badge"><div style="background:var(--orange)"></div></div>
    <div class="badge"><div style="background:var(--red)"></div></div>
    <div class="badge"><div style="background:var(--green)"></div></div>
    <div class="badge"><div style="background:#f2c200"></div></div>
  </div>
  <svg class="arrow" style="left:1110px" width="30" height="20"><path d="M2 10h25M19 2l8 8-8 8" fill="none" stroke="#333" stroke-width="2.5"/></svg>
</section>

<footer class="site-footer">
  <div class="f-about">
    <div class="f-brand"><span class="brand-dot"></span><span>SAHARA HARVEST</span></div>
    <p>Founded in 1980, we grow on decades of trade experience across the region.</p>
    <span class="readmore">READ MORE</span>
    <div class="f-social"><i></i><i></i><i></i><i></i><i></i></div>
  </div>
  <div class="f-col" style="left:540px">
    <h5>Quick Link</h5>
    <ul><li>Home</li><li>About us</li><li>Products</li><li>Services</li><li>Our Team</li><li>Contact us</li></ul>
  </div>
  <div class="f-col f-contact" style="left:800px">
    <h5>Contact us</h5>
    <ul>
      <li><svg width="12" height="12" viewBox="0 0 12 12"><path d="M2 1h3l1 3-2 1a7 7 0 0 0 3 3l1-2 3 1v3c-6 0-9-3-9-9z" fill="#f7a400"/></svg>+000 (0) 123 4567</li>
      <li><svg width="12" height="12" viewBox="0 0 12 12"><path d="M2 1h3l1 3-2 1a7 7 0 0 0 3 3l1-2 3 1v3c-6 0-9-3-9-9z" fill="#f7a400"/></svg>+000 (0) 123 4568</li>
      <li><svg width="12" height="12" viewBox="0 0 12 12"><rect x="1" y="2.5" width="10" height="7" fill="none" stroke="#f7a400"/><path d="M1 3l5 4 5-4" fill="none" stroke="#f7a400"/></svg>hello@saharaharvest.example</li>
      <li><svg width="12" height="12" viewBox="0 0 12 12"><path d="M6 11S2 7 2 4.5a4 4 0 0 1 8 0C10 7 6 11 6 11z" fill="#f7a400"/></svg>Sahara Harvest General Trading LLC</li>
      <li style="padding-left:20px">Unit 12, Green Market Road, Riverton</li>
    </ul>
  </div>
  <div class="bottom"><span>Copyright © 2018 Sahara Harvest General Trading LLC. All rights reserved.</span><span>Privacy Policy · Terms &amp; conditions</span></div>
</footer>

</body>
</html>
```